Redesign of a growing event production company in atlanta!

www.qvrstaging.com - it's Plonko.com site and I'd like to keep it within PLONKO if possible.
We purchased a new logo and we are looking for a redesign.
We specialize in many different aspects of the event production industry and we want our page to be better segmented, with separation between the audio video lighting and wedding services offered.
We also want this cleaned up, showcasing client feedback and highlighted photos. Our industry is very visual and we want some of our work showcased as well as area for event videos.
We want the ability to add new photos and videos as well as links to our blog. If we can incorporate our blog into the site, that would be great as well.
Attached is the new logo, we are going to have it animated and placed on the site as well. We love the color spectrum of light and the significance to event production. We would like the page to incorporate that.

Target Market(s)

Women are the main purchasees of our services. brides between 20 - 40, and then corporate event planners...we have a high end market. We are marketing to the people who plan galas and society socials.

Industry/Entity Type

It Company

Number of Pages Required

5+ page

Font styles to use
Sans Serif
Script

Requirements
Must have
• incorporate the same content I currently have on my site.
• A clear but fluid separation between our event production services (Audio Visual) and the wedding services we offer. We MUST also be able to clearly show what we do. We are a one stop show and we want to convey that.
Nice to have
• Color palette based off logo attached

```html
<!DOCTYPE html>
<html lang="en">
<head>
<meta charset="utf-8">
<title>Lumora Events</title>
<link href="https://fonts.googleapis.com/css2?family=Montserrat:wght@400;500;600&family=Roboto:ital,wght@0,400;0,500;1,400&display=swap" rel="stylesheet">
<style>
:root{
  --black:#0b0b0c;
  --header:#0d0d0f;
  --plum:#7a0f4f;
  --plum-dark:#5e0a3c;
  --blush:#ede3ec;
  --text:#333;
  --muted:#6a6a6a;
  --blue:#2e8fd6;
  --white:#fff;
  --footer:#141416;
}
*{margin:0;padding:0;box-sizing:border-box}
html,body{width:1200px;height:2192px;overflow:hidden}
body{position:relative;background:var(--white);font-family:'Roboto',sans-serif;color:var(--text)}
.abs{position:absolute}
.heading{font-family:'Montserrat',sans-serif;font-weight:400;text-transform:uppercase;text-align:center;letter-spacing:.5px}

/* header */
.site-header{left:0;top:0;width:1200px;height:139px;background:var(--header)}
.spectrum{left:0;top:0;width:1200px;height:3px;background:linear-gradient(90deg,#222 0 20%,#c9c12a 20% 40%,#2a8fd0 40% 60%,#c3224a 60% 80%,#8fbf2a 80%)}
.brand{left:131px;top:30px;display:flex;flex-direction:column;align-items:center;width:140px}
.brand-mark{width:44px;height:44px;border-radius:50%;border:2px solid #ddd}
.brand-name{font-family:'Montserrat',sans-serif;font-size:14px;font-weight:500;color:#e8e8e8;margin-top:6px;letter-spacing:.5px;white-space:nowrap}
.contact-line{top:22px;left:850px;display:flex;gap:22px;font-size:13px;color:#ddd;align-items:center}
.contact-line span{display:flex;align-items:center;gap:7px}
.header-rule{left:421px;top:56px;width:667px;height:1px;background:#2a2a2c}
.main-nav{left:421px;top:77px;display:flex;align-items:center;font-family:'Montserrat',sans-serif;font-size:11px;color:#ddd;text-transform:uppercase}
.main-nav .active{background:var(--plum);color:#fff;width:117px;height:40px;display:flex;align-items:center;justify-content:center;border:1px solid #b33a80}
.main-nav a{position:absolute;white-space:nowrap}

/* hero */
.hero{left:0;top:139px;width:1200px;height:587px;background:radial-gradient(ellipse at 55% 75%,#3a2fa0 0%,#1f1a5a 35%,#120f2a 70%),#120f2a}
.hero-title{left:0;top:451px;width:1200px;font-size:41px;color:#fff;text-shadow:0 2px 6px rgba(0,0,0,.5)}
.thumb-strip{left:113px;top:555px;width:973px;height:132px;background:rgba(10,10,20,.75)}
.thumb{top:570px;width:193px;height:102px}
.thumb.current{outline:2px solid #b0247a}
.pointer{left:258px;top:561px}

/* welcome */
.welcome-title{left:0;top:760px;width:1200px;font-size:26px;color:#222}
.welcome-copy{left:150px;top:802px;width:900px;font-size:12px;line-height:20.5px;color:#444;text-align:center}
.btn{background:var(--plum);color:#fff;font-family:'Montserrat',sans-serif;font-size:12px;text-transform:uppercase;display:flex;align-items:center;justify-content:center;border-radius:2px}

/* events */
.events{left:0;top:976px;width:1200px;height:293px;background:var(--blush)}
.section-title{font-size:24px}
.event-photo{left:117px;top:1070px;width:126px;height:126px;border-radius:50%;border:3px solid #fff;box-shadow:0 0 0 1px #ccc;background:radial-gradient(circle,#d8c29a,#6b5232)}
.event-date{left:120px;top:1211px;width:120px;text-align:center;font-size:12px;color:#444}
.event-loc{left:272px;top:1078px;font-size:11.5px;color:#444;text-transform:uppercase;display:flex;gap:4px;align-items:center}
.event-head{left:272px;top:1104px;font-size:15px;color:var(--plum)}
.event-body{left:272px;top:1132px;width:800px;font-size:11.5px;line-height:26px;color:#666}

/* portfolio */
.portfolio{left:0;top:1269px;width:1200px;height:437px;background:radial-gradient(ellipse at 50% 40%,#1e1e22,#0a0a0b)}
.work{top:1375px;width:224px;height:138px;border:3px solid #fff}
.work-name{top:1527px;width:224px;text-align:center;font-family:'Montserrat',sans-serif;font-size:13px;color:#eee;text-transform:uppercase}
.work-date{top:1553px;width:224px;text-align:center;font-size:13px;color:var(--blue);font-style:italic}

/* blog */
.blog-card{top:1783px;width:325px;height:219px;overflow:hidden;box-shadow:0 12px 14px -10px rgba(0,0,0,.45)}
.blog-disc{position:absolute;left:52px;top:0;width:220px;height:220px;border-radius:50%;background:rgba(12,12,14,.82);text-align:center;color:#fff}
.blog-date{margin-top:42px;font-size:15px}
.blog-title{margin-top:14px;font-family:'Montserrat',sans-serif;font-size:13px;font-weight:500;text-transform:uppercase}
.blog-text{margin:8px auto 0;width:170px;font-size:11.5px;line-height:20px;color:#ccc;padding-bottom:10px;border-bottom:1px solid #555}
.blog-share{display:flex;justify-content:center;gap:4px;margin-top:12px}
.blog-share i{width:15px;height:15px;border-radius:50%;display:block}

/* connect */
.connect{left:0;top:2049px;width:1200px;height:62px;background:var(--black)}
.connect-label{left:240px;top:2068px;font-family:'Montserrat',sans-serif;font-size:19px;color:#fff}
.tile{top:2049px;width:69px;height:62px;display:flex;align-items:center;justify-content:center;font-family:'Roboto',sans-serif;font-size:12px;font-weight:500;color:#fff}
.site-footer{left:0;top:2111px;width:1200px;height:81px;background:var(--footer)}
.footer-links{left:111px;top:2145px;font-size:12px;color:#8ab6d8}
.footer-links b{font-weight:400;color:#888;margin:0 7px}
.copyright{right:111px;top:2145px;font-size:12px;color:#999}
</style>
</head>
<body>

<header class="site-header abs"></header>
<div class="spectrum abs"></div>
<div class="brand abs"><div class="brand-mark"></div><div class="brand-name">LUMORA EVENTS</div></div>
<div class="contact-line abs">
  <span><svg width="12" height="12" viewBox="0 0 12 12"><rect width="12" height="12" rx="2" fill="#2e8fd6"/><path d="M3.5 3h1.6l.6 1.6-.9.7a5 5 0 0 0 2 2l.7-.9 1.6.6V8.6A1.3 1.3 0 0 1 7.7 9.4 5.5 5.5 0 0 1 2.6 4.3 1.3 1.3 0 0 1 3.5 3z" fill="#fff"/></svg>888.555.0142</span>
  <span><svg width="12" height="12" viewBox="0 0 12 12"><rect width="12" height="12" rx="2" fill="#2e8fd6"/><rect x="3" y="3" width="6" height="6" fill="#fff"/></svg>(678)555-0199</span>
</div>
<div class="header-rule abs"></div>
<nav class="main-nav abs">
  <span class="active">Get Inspired!</span>
  <a style="left:152px">Services Offered</a>
  <a style="left:305px">Lumora Owners</a>
  <a style="left:448px">Client Referrals</a>
  <a style="left:602px">Contact</a>
</nav>

<section class="hero abs" role="img" aria-label="Crowd dancing at a nightclub event behind a DJ mixing console under purple lights"></section>
<h1 class="hero-title heading abs">Lumora Event Production</h1>
<div class="thumb-strip abs"></div>
<svg class="abs" style="left:136px;top:612px" width="14" height="18" viewBox="0 0 14 18"><path d="M10 2 3 9l7 7" stroke="#fff" stroke-width="3" fill="none"/></svg>
<svg class="abs" style="left:1049px;top:612px" width="14" height="18" viewBox="0 0 14 18"><path d="M4 2l7 7-7 7" stroke="#fff" stroke-width="3" fill="none"/></svg>
<svg class="pointer abs" width="16" height="9" viewBox="0 0 16 9"><path d="M0 9 8 0l8 9z" fill="#b0247a"/></svg>
<div class="thumb current abs" style="left:171px;background:linear-gradient(#2a2470,#0e0c24)" role="img" aria-label="DJ booth with blue stage lighting"></div>
<div class="thumb abs" style="left:392px;background:linear-gradient(#4a4030,#1b1812)" role="img" aria-label="Guests dancing under a spotlight"></div>
<div class="thumb abs" style="left:614px;background:linear-gradient(#7a4a22,#2a1a10)" role="img" aria-label="Overhead view of a packed dance floor"></div>
<div class="thumb abs" style="left:835px;background:linear-gradient(#e07a20,#5a1808)" role="img" aria-label="Concert crowd under orange stage lights"></div>

<h2 class="welcome-title heading abs">Welcome to Lumora Events</h2>
<p class="welcome-copy abs">Lumora Events is an award winning event production company providing quality, custom event solutions catered to your specific needs from planning and entertainment to audio, video and lighting.<br>Lumora Event Production's team has diverse professional experience working in professional Entertainment, Catering, Audio/Video Production, Venue Management and Lighting Production. This seperates us from our competition, giving you the best event experience!</p>
<div class="btn abs" style="left:510px;top:902px;width:180px;height:49px">View our live stream!</div>

<section class="events abs"></section>
<h2 class="heading section-title abs" style="left:0;top:1017px;width:1200px;color:#222">Latest Events</h2>
<svg class="abs" style="left:76px;top:1126px" width="12" height="18" viewBox="0 0 12 18"><path d="M9 2 3 9l6 7" stroke="#555" stroke-width="2" fill="none"/></svg>
<svg class="abs" style="left:1109px;top:1126px" width="12" height="18" viewBox="0 0 12 18"><path d="M3 2l6 7-6 7" stroke="#555" stroke-width="2" fill="none"/></svg>
<div class="event-photo abs" role="img" aria-label="Couple's first dance in a chandelier-lit ballroom"></div>
<div class="event-date abs"><svg width="11" height="11" viewBox="0 0 11 11"><rect x=".5" y="1.5" width="10" height="9" fill="none" stroke="#2e8fd6"/><rect x=".5" y="1.5" width="10" height="3" fill="#2e8fd6"/></svg> MAR 26 2015</div>
<div class="event-loc abs"><svg width="9" height="12" viewBox="0 0 9 12"><path d="M4.5 0A4.5 4.5 0 0 0 0 4.5C0 8 4.5 12 4.5 12S9 8 9 4.5A4.5 4.5 0 0 0 4.5 0z" fill="#2e8fd6"/><circle cx="4.5" cy="4.5" r="1.6" fill="#ede3ec"/></svg>Lorem ipsum dolor</div>
<div class="event-head abs">Ut wisi enim ad minim veniam, quis nostrud exerci tation ullamcorper suscipit</div>
<p class="event-body abs">Duis autem vel eum iriure dolor in hendrerit in vulputate velit esse molestie consequat, vel illum dolore eu feugiat nulla facilisis at vero eros et accumsan et iusto odio dignissim qui blandit praesent luptatum zzril delenit augue duis dolore te feugait nulla facilisi. Nam liber tempor cum soluta nobis eleifend option congue nihil imperdiet doming id quod mazim placerat facer possim assum.</p>

<section class="portfolio abs"></section>
<h2 class="heading section-title abs" style="left:0;top:1312px;width:1200px;color:#fff">Our Portfolio</h2>
<div class="work abs" style="left:113px;background:linear-gradient(#6f8a4a,#8a7a66)" role="img" aria-label="Bride and groom walking down a stone garden path"></div>
<div class="work abs" style="left:362px;background:linear-gradient(#2a2a2e,#0e0e10)" role="img" aria-label="Corporate event signage wall"></div>
<div class="work abs" style="left:612px;background:linear-gradient(#8a7a58,#3a3022)" role="img" aria-label="Wedding dance in a grand ballroom"></div>
<div class="work abs" style="left:864px;background:linear-gradient(#b07aa0,#2a1a28)" role="img" aria-label="DJ stage draped in white with pink uplighting"></div>
<div class="work-name abs" style="left:113px">Epsum factorial non</div>
<div class="work-name abs" style="left:362px">Typi non habent</div>
<div class="work-name abs" style="left:612px">Habent claritatem insitam</div>
<div class="work-name abs" style="left:864px">Claritas est etiam</div>
<div class="work-date abs" style="left:113px">20/03/2015</div>
<div class="work-date abs" style="left:362px">20/03/2015</div>
<div class="work-date abs" style="left:612px">20/03/2015</div>
<div class="work-date abs" style="left:864px">20/03/2015</div>
<div class="btn abs" style="left:510px;top:1605px;width:180px;height:50px">View more gallery</div>

<h2 class="heading section-title abs" style="left:0;top:1739px;width:1200px;color:#222">Latest from the blog</h2>
<article class="blog-card abs" style="left:113px;background:linear-gradient(90deg,#3a2a1a,#8a6a3a)" role="img" aria-label="Groom standing in a warmly lit venue doorway">
  <div class="blog-disc"><div class="blog-date">24/02/2015</div><div class="blog-title">Pellentesque sed dolor</div><div class="blog-text">Fusce euismod consequat ante. Lorem ipsum dolor sit amet, consectetuer.</div><div class="blog-share"><i style="background:#3b5b99"></i><i style="background:#2aa3e0"></i><i style="background:#d8473a"></i></div></div>
</article>
<article class="blog-card abs" style="left:438px;background:linear-gradient(#1a2a4a,#3a2a2a)" role="img" aria-label="Evening crowd outside a lit reception hall">
  <div class="blog-disc"><div class="blog-date">23/02/2015</div><div class="blog-title">Lorem ipsum dolor sit</div><div class="blog-text">Fusce euismod consequat ante. Lorem ipsum dolor sit amet, consectetuer.</div><div class="blog-share"><i style="background:#3b5b99"></i><i style="background:#2aa3e0"></i><i style="background:#d8473a"></i></div></div>
</article>
<article class="blog-card abs" style="left:762px;background:linear-gradient(#4a2a7a,#8a5ab0)" role="img" aria-label="Reception tables under purple uplighting">
  <div class="blog-disc"><div class="blog-date">19/02/2015</div><div class="blog-title">Typi non habent clari</div><div class="blog-text">Fusce euismod consequat ante. Lorem ipsum dolor sit amet, consectetuer.</div><div class="blog-share"><i style="background:#3b5b99"></i><i style="background:#2aa3e0"></i><i style="background:#d8473a"></i></div></div>
</article>

<section class="connect abs"></section>
<div class="connect-label abs">CONNECT US :</div>
<a class="tile abs" style="left:412px;background:#4a9a3a">Tripnest</a>
<a class="tile abs" style="left:481px;background:#2a8fc8">Vidlo</a>
<a class="tile abs" style="left:550px;background:#2f5f8a">Snapla</a>
<a class="tile abs" style="left:619px;background:#c81e1e">Tubio</a>
<a class="tile abs" style="left:688px;background:#1f6fa8">Linkly</a>
<a class="tile abs" style="left:757px;background:#c8102e">Pinbo</a>
<a class="tile abs" style="left:826px;background:#3b5b99">Facio</a>

<footer class="site-footer abs"></footer>
<div class="footer-links abs">Home<b>|</b>About Us<b>|</b>Contact Us<b>|</b>Privacy Policy<b>|</b>Sitemap</div>
<div class="copyright abs">Copyright © 2015 Lumora Events. All rights reserved</div>

</body>
</html>
```